Assessment Report cover design and formatting

This report is for senior executives and provides leaders with detailed insight into their capabilities and skills. The cover should have space for the date and name of the person doing the assessment. We are looking to modernise the report cover design. We would like the report to be our company colours if possible. The work will likely expand once the cover is done to other parts of the report, ie. the format and layout of the report etc.

Company colours:
Primary colours:
• Blue #0D47A1, #115CD0, #90B6ED, #EEf3FB
• Green #0D91A1, #47A10D, #324C196, #0DA11D
Additional colours:
• Purple #A10D91
• Brown #A1670D
• Red #A10D47

Target Market(s)

Executives

Industry/Entity Type

Consulting, leadership development

Colors
0094D4
00A9DD
6FCCEA
C7EBF8
E9F6FB
00AB8E
00BBA5
67D7C9
C6EFE9
E9F9F6
E54698
E96AAD
F1A4CE
F9D9EA
FCEFF6
6B429C
8869AF
B7A5CE
E3DAEB
F3F0F8

Requirements
Must have
• The report cover should have space for name of user, the date and company logo. Cover should be in A4 size.

```html
<!DOCTYPE html>
<html lang="en">
<head>
<meta charset="utf-8">
<title>Growth Leader Assessment – Insight Report Cover</title>
<link href="https://fonts.googleapis.com/css2?family=Poppins:wght@400;500;600&display=swap" rel="stylesheet">
<style>
  :root {
    --paper: #ffffff;
    --backdrop: #e4e4e4;
    --navy: #0D47A1;
    --sky: #90B6ED;
    --mint: #7BE6BE;
    --teal: #22C9A8;
    --petrol: #1A8EA6;
    --green: #47A10D;
    --ink: #1B3F94;
  }
  * { margin: 0; padding: 0; box-sizing: border-box; }
  html, body {
    width: 849px; height: 1200px; overflow: hidden;
    background: var(--backdrop);
  }
  .cover {
    position: relative;
    width: 849px; height: 1200px;
    background: linear-gradient(180deg, #f4f4f4 0%, var(--paper) 35%);
    font-family: "Poppins", sans-serif;
    color: var(--ink);
    overflow: hidden;
  }
  .cover-art { position: absolute; inset: 0; }
  .confidential {
    position: absolute; left: 81px; top: 84px;
    font-size: 16px; font-weight: 400; letter-spacing: 3px;
    color: var(--ink);
    padding-bottom: 4px;
    border-bottom: 3px solid var(--green);
  }
  .brand {
    position: absolute; left: 81px; top: 168px;
    display: flex; align-items: center; gap: 8px;
    font-size: 17px; font-weight: 500; color: var(--navy);
  }
  .brand-dot {
    width: 14px; height: 14px; border-radius: 50%;
    background: var(--petrol);
  }
  .recipient {
    position: absolute; left: 81px; top: 250px;
    font-size: 13px; line-height: 20px; color: var(--navy);
  }
  .recipient-label { font-weight: 600; }
  .title-block { position: absolute; inset: 0; }
  .report-title {
    position: absolute; left: 79px; top: 666px;
    font-size: 47px; font-weight: 400; letter-spacing: 1px;
    line-height: 1; color: var(--navy);
  }
  .report-subtitle {
    position: absolute; left: 81px; top: 727px;
    font-size: 31px; font-weight: 400; letter-spacing: 1px;
    line-height: 1; color: var(--navy);
  }
</style>
</head>
<body>
  <main class="cover">
    <svg class="cover-art" width="849" height="1200" viewBox="0 0 849 1200">
      <defs>
        <linearGradient id="ribbonTones" x1="0" y1="1" x2="1" y2="0">
          <stop offset="0" stop-color="#1565A8"/>
          <stop offset="0.35" stop-color="#1FB3A6"/>
          <stop offset="0.6" stop-color="#3FE0C4"/>
          <stop offset="1" stop-color="#158AA8"/>
        </linearGradient>
      </defs>
      <polygon role="img" aria-label="Abstract layered ribbons in teal, mint and blue sweeping diagonally across the cover"
        points="0,623 612,261 849,15 849,919 661,1200 0,1200" fill="url(#ribbonTones)"/>
    </svg>

    <p class="confidential">CONFIDENTIAL</p>

    <div class="brand">
      <span class="brand-dot"></span>
      <span class="brand-name">Northbridge Advisory</span>
    </div>

    <div class="recipient">
      <p class="recipient-label">INSIGHT REPORT FOR:</p>
      <p class="recipient-name">Name</p>
      <p class="recipient-date">29 October 2023</p>
    </div>

    <svg class="title-block" width="849" height="1200" viewBox="0 0 849 1200">
      <polygon class="title-panel" points="59,588 539,588 758,816 59,816" fill="var(--paper)"/>
      <g class="title-slashes" fill="var(--navy)">
        <polygon points="81,611 97,611 89,652 81,652"/>
        <polygon points="108,611 124,611 116,652 100,652"/>
        <polygon points="135,611 151,611 143,652 127,652"/>
        <polygon points="162,611 178,611 170,652 154,652"/>
      </g>
      <g class="title-colour-bar">
        <rect x="81" y="783" width="82" height="10" fill="var(--navy)"/>
        <rect x="163" y="783" width="81" height="10" fill="var(--sky)"/>
        <rect x="244" y="783" width="81" height="10" fill="var(--mint)"/>
        <rect x="325" y="783" width="81" height="10" fill="var(--teal)"/>
        <rect x="406" y="783" width="81" height="10" fill="var(--petrol)"/>
      </g>
    </svg>

    <h1 class="report-title">GROWTH LEADER</h1>
    <p class="report-subtitle">ASSESSMENT</p>
  </main>
</body>
</html>
```